"A Touch RMB" Business Card/Logo Design

I'm looking for a very creative look for my new business called "A Touch RMB" on a business card design. Don't be distracted by my "business card details" below....if you have other ideas on how you see "A Touch RMB" go for it. If probably should somehow give a look that I paint furniture....maybe a paint drip or something simple or you can get more creative....sky's the limit and I really need your creative eye on how to per tray that "A Touch RMB" means taking something old and turning into new again with some paint.

Industry/Entity Type

Business

Contact Information for Business Card

I refurbish and up-cycle furniture that needs "a little TLC'....thus, my business name was born called "A Touch RMB" (Those are my initials). I mainly paint old furniture of all styles and bring them back to life. I sometimes recreate furniture as well....I will make benches from old headboards of all sizes, etc. I'd love to see design that incorporate the crafty/creative side of me. If that means incorporating a paint brush, tools, paint cans, or furniture such as dressers, old vintage furniture, spindles, etc, etc. I don't know if something creative could be done with my initials (RMB). I really have a creative block of ideas and need your help bringing my "A Touch RMB" business to life.

P.S. Below is just one picture that I thought was neat and creative as they used a paintbrush but used spindles for the bristles and put their logo in the middle. Just an idea I thought was very unique and creative.

I'm very excited to see your design. Thank you for taking the time to create my logo/business card for me.

Carla

Requirements
Must have
• Please include this information on the card:
• My Name: Carla Brennick
• Address: 14706 318th Ln SE, Fox Hollow, MN 55418
• E-Mail: atouchrmb@mailcove.net
• FB: http:/www.friendpage.net/atouchrmb
• Cell: 763-419-7082

```html
<!DOCTYPE html>
<html lang="en">
<head>
<meta charset="utf-8">
<title>A Touch RMB – Business Card</title>
<link href="https://fonts.googleapis.com/css2?family=Open+Sans:wght@400;600&display=swap" rel="stylesheet">
<style>
  :root {
    --page: #e8e3db;
    --card-dark: #2e170d;
    --card-mid: #4a2a1c;
    --card-light: #5c3829;
    --accent: #f2a31f;
    --accent-deep: #d9861a;
    --accent-pale: #f7c548;
    --stroke-brown: #8a5a22;
    --text-soft: #e3d6c8;
    --text-muted: #a8978a;
  }
  * { margin: 0; padding: 0; box-sizing: border-box; }
  html, body { width: 1200px; height: 1023px; overflow: hidden; }
  body {
    background: var(--page);
    font-family: "Open Sans", Arial, sans-serif;
    position: relative;
  }
  .card {
    position: absolute;
    left: 280px;
    width: 640px;
    height: 366px;
    border-radius: 6px;
    overflow: hidden;
    background: linear-gradient(135deg, var(--card-light) 0%, var(--card-mid) 40%, var(--card-dark) 100%);
    box-shadow: 0 10px 28px rgba(40, 20, 10, 0.28);
  }
  .card--front { top: 110px; }
  .card--back { top: 547px; }

  .brand-name {
    color: var(--accent);
    font-weight: 600;
    white-space: nowrap;
  }

  /* front */
  .brand {
    position: absolute;
    left: 44px;
    top: 44px;
    display: flex;
    align-items: center;
    gap: 10px;
    font-size: 22px;
  }
  .brand__square {
    width: 16px;
    height: 16px;
    background: var(--accent);
    border-radius: 2px;
  }
  .holder {
    position: absolute;
    left: 44px;
    top: 118px;
  }
  .holder__name {
    color: var(--accent);
    font-weight: 600;
    font-size: 30px;
    line-height: 1.1;
  }
  .holder__role {
    color: var(--text-muted);
    font-size: 12px;
    letter-spacing: 1px;
    margin-top: 4px;
  }
  .contacts {
    position: absolute;
    left: 70px;
    top: 196px;
    list-style: none;
  }
  .contacts__item {
    display: flex;
    align-items: center;
    gap: 10px;
    color: var(--text-soft);
    font-size: 14px;
    height: 26px;
  }
  .contacts__icon {
    width: 16px;
    height: 16px;
    border-radius: 3px;
    background: var(--accent);
    display: flex;
    align-items: center;
    justify-content: center;
  }
  .address {
    position: absolute;
    left: 44px;
    bottom: 34px;
    color: var(--text-soft);
    font-size: 13px;
    letter-spacing: 0.5px;
    text-transform: uppercase;
  }
  .stroke-vertical {
    position: absolute;
    right: 0;
    top: 74px;
    width: 96px;
    height: 292px;
    background: linear-gradient(90deg, var(--stroke-brown) 0%, var(--accent-deep) 25%, var(--accent) 55%, var(--accent-pale) 80%, var(--accent-deep) 100%);
  }
  .card-label {
    position: absolute;
  }
  .card-label--front {
    right: 20px;
    top: 30px;
    font-size: 18px;
  }

  /* back */
  .stroke-horizontal {
    position: absolute;
    left: 0;
    top: 140px;
    width: 430px;
    height: 96px;
    background: linear-gradient(180deg, var(--stroke-brown) 0%, var(--accent-deep) 25%, var(--accent) 55%, var(--accent-pale) 80%, var(--accent-deep) 100%);
  }
  .card-label--back {
    left: 452px;
    top: 170px;
    font-size: 24px;
  }
</style>
</head>
<body>
  <section class="card card--front">
    <div class="brand"><span class="brand__square"></span><span class="brand-name">A Touch RMB</span></div>

    <div class="holder">
      <div class="holder__name">Carla Brennick</div>
      <div class="holder__role">DIRECTOR</div>
    </div>

    <ul class="contacts">
      <li class="contacts__item">
        <span class="contacts__icon">
          <svg width="10" height="10" viewBox="0 0 24 24"><path fill="#2e170d" d="M6.6 10.8a15.1 15.1 0 0 0 6.6 6.6l2.2-2.2c.3-.3.7-.4 1-.2 1.1.4 2.3.6 3.6.6.6 0 1 .4 1 1V20c0 .6-.4 1-1 1A17 17 0 0 1 3 4c0-.6.4-1 1-1h3.5c.6 0 1 .4 1 1 0 1.3.2 2.5.6 3.6.1.3 0 .7-.2 1z"/></svg>
        </span>763-419-7082
      </li>
      <li class="contacts__item">
        <span class="contacts__icon"></span>atouchrmb
      </li>
      <li class="contacts__item">
        <span class="contacts__icon">
          <svg width="10" height="8" viewBox="0 0 20 14"><rect x="1" y="1" width="18" height="12" fill="none" stroke="#2e170d" stroke-width="2"/><path d="M1 1l9 7 9-7" fill="none" stroke="#2e170d" stroke-width="2"/></svg>
        </span>atouchrmb@mailcove.net
      </li>
    </ul>

    <div class="address">14706 318th Ln SE, Fox Hollow, MN 55418</div>

    <div class="stroke-vertical" role="img" aria-label="Painted brush stroke in layered gold and amber tones"></div>
    <div class="card-label card-label--front brand-name">A Touch RMB</div>
  </section>

  <section class="card card--back">
    <div class="stroke-horizontal" role="img" aria-label="Painted brush stroke in layered gold and amber tones"></div>
    <div class="card-label card-label--back brand-name">A Touch RMB</div>
  </section>
</body>
</html>
```